Gentle Kindred. a joyful state of being.

adding value to ones circumstance through the teachings of neutralization. quote for back of card: "and then it happens... One day you wake up and you're in this place. You are in this place where everything is right. Your heart is calm. Your soul is lit. Your thoughts are positive. Your vision is clear. Your faith is stronger than ever. And you are at peace. At peace with where you have been. At peace with what you've been through. And at peace with where you're headed." -unknown

Target Market(s)

spiritual, awakening, inspiration, motivation, gratefulness, oneness, peace, positive mindset,

Contact Information for Business Card

front: one line message from quote

Logo Text

up to suggestions

Font styles to use
Serif
Sans Serif
Script

Colors

Designer to choose colors to be used in the design.

Requirements
Must have
• entire quote on one side of card
Nice to have
• simple, and to the point
Should not have
• elaborated designs

```html
<!DOCTYPE html>
<html lang="en">
<head>
<meta charset="utf-8">
<title>Gentle Kindred – Business Card</title>
<link href="https://fonts.googleapis.com/css2?family=Oswald:wght@200;300;400;500&family=Josefin+Sans:ital,wght@0,300;0,400;1,300;1,400&display=swap" rel="stylesheet">
<style>
  :root {
    --purple: #5b2a91;
    --red: #e3212b;
    --ink: #555a60;
    --card: #ffffff;
    --bg-light: #f7f7f8;
    --bg-mid: #e6e6e8;
  }
  * { box-sizing: border-box; margin: 0; padding: 0; }
  html, body { width: 1200px; height: 1200px; overflow: hidden; }
  body {
    background: radial-gradient(ellipse at 50% 40%, var(--bg-light) 0%, var(--bg-mid) 100%);
    position: relative;
    font-family: "Josefin Sans", sans-serif;
  }

  .brand {
    display: flex; align-items: center; gap: 14px;
    font-family: "Oswald", sans-serif; font-weight: 300;
    color: var(--purple); letter-spacing: 1px; white-space: nowrap;
  }
  .brand-dot { border-radius: 50%; background: var(--red); flex: none; }

  .hero-brand {
    position: absolute; top: 140px; left: 0; width: 1200px;
    justify-content: center; font-size: 82px; gap: 22px;
  }
  .hero-brand .brand-dot { width: 30px; height: 30px; }

  .card {
    position: absolute; left: 290px; width: 620px; height: 300px;
    background: var(--card);
    box-shadow: 0 3px 0 #d8d8d8, 0 6px 0 #cfcfcf, 0 14px 24px rgba(0,0,0,.12);
  }

  /* quote side */
  .card-quote { top: 380px; text-align: center; }
  .card-quote .brand { justify-content: center; font-size: 32px; margin-top: 28px; gap: 10px; }
  .card-quote .brand-dot { width: 12px; height: 12px; }
  .quote {
    margin: 14px 38px 0; font-style: italic; font-weight: 300;
    font-size: 15.5px; line-height: 1.16; letter-spacing: .4px;
  }
  .quote .lead { display: block; font-style: normal; color: var(--red); margin-bottom: 2px; }
  .quote .mark { color: var(--purple); font-family: Georgia, serif; font-weight: 700; font-style: normal; font-size: 22px; line-height: 0; }
  .p { color: var(--purple); }
  .r { color: var(--red); }
  .attribution {
    position: absolute; left: 0; right: 0; bottom: 22px;
    display: flex; align-items: center; gap: 22px;
    color: var(--red); font-size: 18px; letter-spacing: 1px;
  }
  .attribution::before, .attribution::after { content: ""; flex: 1; height: 1px; background: var(--red); }

  /* contact side */
  .card-contact { top: 730px; }
  .card-contact .brand { position: absolute; left: 40px; top: 30px; font-size: 30px; gap: 10px; }
  .card-contact .brand-dot { width: 12px; height: 12px; }
  .person { position: absolute; left: 38px; top: 108px; }
  .person-name { font-family: "Oswald", sans-serif; font-weight: 300; color: var(--red); font-size: 19px; letter-spacing: 3px; }
  .person-title { color: var(--purple); font-size: 15px; letter-spacing: 2px; }
  .contacts { position: absolute; left: 32px; bottom: 26px; list-style: none; color: var(--ink); font-size: 13px; letter-spacing: .5px; }
  .contacts li { display: flex; align-items: center; gap: 8px; height: 22px; }
  .contacts svg { width: 11px; height: 11px; fill: var(--red); }

  .rules { position: absolute; left: 330px; top: 0; width: 20px; height: 160px; }
  .slogan {
    position: absolute; left: 378px; top: 10px;
    font-family: "Oswald", sans-serif; font-size: 88px; line-height: 0.93;
    letter-spacing: 4px;
  }
  .slogan .thin { font-weight: 200; color: var(--purple); }
  .slogan .bold-red { font-weight: 400; color: var(--red); }
  .slogan .bold-purple { font-weight: 500; color: var(--purple); }
</style>
</head>
<body>

  <div class="brand hero-brand">GENTLE KINDRED<span class="brand-dot"></span></div>

  <section class="card card-quote">
    <div class="brand">GENTLE KINDRED<span class="brand-dot"></span></div>
    <p class="quote">
      <span class="lead"><span class="mark">“</span> and then it happens...</span>
      <span class="p">One day you wake up and you're in this place.</span>
      <span class="r">You are in this place where everything is right.</span>
      <span class="p">Your heart is calm.</span>
      <span class="r">Your soul is lit.</span>
      <span class="p">Your thoughts are positive.</span>
      <span class="r">Your vision is clear.</span>
      <span class="p">Your faith is stronger than ever.</span>
      <span class="r">And you are at peace.</span>
      <span class="p">At peace with where you have been.</span>
      <span class="r">At peace with what you've been through.</span>
      <span class="p">And at peace with where you're headed.</span>
      <span class="mark">”</span>
    </p>
    <div class="attribution">unknown</div>
  </section>

  <section class="card card-contact">
    <div class="brand">GENTLE KINDRED<span class="brand-dot"></span></div>
    <div class="person">
      <div class="person-name">YOUR NAME</div>
      <div class="person-title">Titel</div>
    </div>
    <ul class="contacts">
      <li><svg viewBox="0 0 24 24"><path d="M6.6 10.8a15 15 0 0 0 6.6 6.6l2.2-2.2c.3-.3.7-.4 1-.2 1.1.4 2.3.6 3.6.6.6 0 1 .4 1 1V20c0 .6-.4 1-1 1A17 17 0 0 1 3 4c0-.6.4-1 1-1h3.5c.6 0 1 .4 1 1 0 1.3.2 2.5.6 3.6.1.3 0 .7-.2 1z"/></svg>000 000 122 445</li>
      <li><svg viewBox="0 0 24 24"><path d="M2 5h20v2l-10 6L2 7zm0 4.3 10 6 10-6V19H2z"/></svg>info@gentlekindred.com</li>
      <li><svg viewBox="0 0 24 24"><path d="M12 2a10 10 0 1 0 0 20 10 10 0 0 0 0-20zm6.9 9h-3a15 15 0 0 0-1.3-6 8 8 0 0 1 4.3 6zM12 4c.9 1.2 1.7 3.7 1.9 7h-3.8c.2-3.3 1-5.8 1.9-7zM9.4 5a15 15 0 0 0-1.3 6h-3a8 8 0 0 1 4.3-6zM5.1 13h3a15 15 0 0 0 1.3 6 8 8 0 0 1-4.3-6zm6.9 7c-.9-1.2-1.7-3.7-1.9-7h3.8c-.2 3.3-1 5.8-1.9 7zm2.6-1a15 15 0 0 0 1.3-6h3a8 8 0 0 1-4.3 6z"/></svg>www.gentlekindred.com</li>
    </ul>
    <svg class="rules" viewBox="0 0 20 160" aria-hidden="true">
      <line x1="2" y1="0" x2="2" y2="120" stroke="var(--purple)" stroke-width="1.5"/>
      <line x1="9" y1="0" x2="9" y2="150" stroke="var(--purple)" stroke-width="1.5"/>
    </svg>
    <div class="slogan">
      <div class="thin">YOUR</div>
      <div class="bold-red">SOUL</div>
      <div><span class="thin">IS</span> <span class="bold-purple">LIT</span></div>
    </div>
  </section>

</body>
</html>
```